Fern Lusk medical cannibis cultivation company

tag - Lusk grow
Fern Lusk medical cannabis cultivation - logo is selected- can we please see bold examples with our selection. We are mainly dealing with medical companies and professionals. We would like to be stand out in the crowd with our designs. Welcome any and all attempts. Thanks

Target Market(s)

Medical and Professional

Industry/Entity Type

Medical And Science

Font styles to use
Sans Serif

Colors

Designer to choose colors to be used in the design.

Requirements
Must have
• Bright colour and be bold- Love the teal and magenta that is currently on the dark background design.
Nice to have
• shading and the 3D affect- The shadowed appearance.
Should not have
• Anything related to illegal activity or un professional manners

```html
<!DOCTYPE html>
<html lang="en">
<head>
<meta charset="utf-8">
<title>Fern Lusk Stationery</title>
<link href="https://fonts.googleapis.com/css2?family=Open+Sans:wght@400;600;700&family=Marcellus&display=swap" rel="stylesheet">
<style>
  :root {
    --teal: #14a9b8;
    --magenta: #e23a8c;
    --mauve: #bd6c98;
    --ink: #3e3e44;
    --grey: #8a8d92;
    --paper: #ffffff;
    --backdrop: #efefef;
    --card-a: #4d9db0;
    --card-b: #d95c98;
    --shadow: 2px 4px 10px rgba(0, 0, 0, 0.32), 0 0 1px rgba(0, 0, 0, 0.25);
  }
  * { margin: 0; padding: 0; box-sizing: border-box; }
  html, body { width: 1200px; height: 1200px; overflow: hidden; }
  body {
    background: linear-gradient(180deg, #f8f8f8, #e6e6e7);
    font-family: "Open Sans", sans-serif;
    color: var(--ink);
    position: relative;
  }
  .sheet { position: absolute; }
  .backing-sheet { left: 93px; top: 102px; width: 717px; height: 926px; background: var(--mauve); box-shadow: var(--shadow); }

  .letterhead { left: 128px; top: 138px; width: 717px; height: 927px; background: var(--paper); box-shadow: var(--shadow); overflow: hidden; }
  .brand-mark {
    display: flex; align-items: center; gap: 8px;
    font-family: "Marcellus", serif; color: var(--teal);
    letter-spacing: 0.5px; white-space: nowrap;
  }
  .brand-mark .dot { width: 12px; height: 12px; border-radius: 50%; background: var(--magenta); }
  .letterhead .brand-mark { position: absolute; top: 92px; left: 0; width: 100%; justify-content: center; font-size: 28px; }
  .letter-body { position: absolute; left: 62px; top: 200px; width: 600px; font-size: 12.5px; line-height: 24px; }
  .letter-body p { margin-bottom: 24px; }
  .letter-body .address p { margin: 0; }
  .letter-close { position: absolute; left: 60px; top: 676px; font-size: 12.5px; }
  .signature { position: absolute; left: 58px; top: 696px; width: 140px; height: 46px; background: linear-gradient(90deg, #d9d9dc, #ededef); border-radius: 4px; }
  .letter-footer { position: absolute; left: 0; top: 858px; width: 100%; text-align: center; }
  .letter-footer .company { font-family: "Marcellus", serif; color: var(--magenta); font-size: 13px; letter-spacing: 0.3px; }
  .letter-footer .rule { margin: 8px auto 6px; width: 610px; height: 1px; background: #c9c9cc; }
  .letter-footer .contact { font-family: "Marcellus", serif; color: #555; font-size: 14.5px; white-space: nowrap; }

  .envelope { left: 331px; top: 536px; width: 782px; height: 340px; background: var(--paper); box-shadow: var(--shadow); }
  .envelope .brand-mark { position: absolute; left: 43px; top: 238px; font-size: 28px; }
  .envelope .return-address { position: absolute; left: 39px; top: 294px; font-family: "Marcellus", serif; color: var(--magenta); font-size: 17px; }

  .card { width: 346px; height: 198px; box-shadow: var(--shadow); }
  .card-front { left: 712px; top: 210px; background: linear-gradient(100deg, var(--card-a), #9486a8 50%, var(--card-b)); overflow: hidden; }
  .card-front .frame { position: absolute; left: 30px; top: 20px; width: 286px; height: 158px; border: 3px solid #f4f4f6; border-radius: 26px; box-shadow: 0 1px 3px rgba(0,0,0,0.3); }
  .card-front .holder { position: absolute; top: 50px; width: 100%; text-align: center; color: #fff; font-size: 14.5px; font-weight: 600; letter-spacing: 0.6px; }
  .card-front .band { position: absolute; left: 14px; top: 79px; width: 318px; height: 54px; background: #fff; text-align: center; color: #222; padding-top: 5px; box-shadow: 0 1px 3px rgba(0,0,0,0.25); }
  .card-front .band .company { font-size: 8px; font-weight: 700; letter-spacing: 0.7px; margin-bottom: 6px; }
  .card-front .band .line { font-size: 8px; font-weight: 600; line-height: 12px; }
  .card-front .location { position: absolute; top: 142px; width: 100%; text-align: center; color: #fff; font-size: 8.5px; font-weight: 600; letter-spacing: 0.3px; }

  .card-back { left: 713px; top: 464px; background: var(--paper); }
  .card-back .border { position: absolute; left: 10px; top: 6px; width: 326px; height: 186px; border: 1px solid var(--magenta); }
  .card-back .border::after { content: ""; position: absolute; left: 3px; top: 3px; right: 3px; bottom: 3px; border: 1px solid var(--magenta); }
  .card-back .corner { position: absolute; width: 8px; height: 8px; background: var(--magenta); }
  .card-back .brand-mark { position: absolute; left: 0; top: 84px; width: 100%; justify-content: center; font-size: 22px; }
</style>
</head>
<body>
  <div class="sheet backing-sheet"></div>

  <section class="sheet letterhead">
    <div class="brand-mark"><span class="dot"></span>FERN LUSK</div>
    <div class="letter-body">
      <div class="address"><p>To</p><p>The,</p><p>Director</p></div>
      <p style="margin-top:24px">Lorem ipsum dolor sit amet, consectetur adipiscing elit. Sed at ante. Mauris eleifend, quam a vulputate dictum, massa quam dapibus leo, eget vulputate orci purus ut lorem. In fringilla mi in ligula. Pellentesque aliquam quam vel dolor. Nunc adipiscing. Sed quam odio, tempus ac, aliquam molestie varius ac, tellus. Vestibulum ut nulla aliquam risus rutrum interdum. Pellentesque lorem.</p>
      <p>Curabitur sit amet erat quis risus feugiat viverra. Pellentesque augue justo, sagittis et, lacinia at, venenatis non, arcu. Nunc nec libero. In cursus dictum risus. Etiam tristique nisl a nulla. Curabitur dolor nunc, egestas at, accumsan at, malesuada nec, magna. Vestibulum ante ipsum primis in faucibus orci luctus et ultrices posuere cubilia curae; orci vel mauris blandit vehicula.</p>
      <p>In hac habitasse platea dictumst. Nulla facilisi. Fusce ac dolor, sed imperdiet nulla erat sit amet, elit.</p>
    </div>
    <div class="letter-close">Thanking you,</div>
    <div class="signature" role="img" aria-label="Handwritten signature of Nora Vale"></div>
    <div class="letter-footer">
      <div class="company">FERN LUSK MEDICAL CANNABIS CULTIVATION</div>
      <div class="rule"></div>
      <div class="contact">123-456-7890 | www.fernlusk.com | nora@fernlusk.com | Dummy city, Dummy country land</div>
    </div>
  </section>

  <section class="sheet card card-front">
    <div class="frame"></div>
    <div class="holder">NORA VALE | Director</div>
    <div class="band">
      <div class="company">FERN LUSK MEDICAL CANNABIS CULTIVATION</div>
      <div class="line">123-456-7890</div>
      <div class="line">www.fernlusk.com | nora@fernlusk.com</div>
    </div>
    <div class="location">Dummy city, Dummy country land</div>
  </section>

  <section class="sheet envelope">
    <div class="brand-mark"><span class="dot"></span>FERN LUSK</div>
    <div class="return-address">Dummy city, Dummy country land</div>
  </section>

  <section class="sheet card card-back">
    <div class="border"></div>
    <span class="corner" style="left:7px;top:4px"></span>
    <span class="corner" style="right:7px;top:4px"></span>
    <span class="corner" style="left:7px;bottom:4px"></span>
    <span class="corner" style="right:7px;bottom:4px"></span>
    <div class="brand-mark"><span class="dot"></span>FERN LUSK</div>
  </section>
</body>
</html>
```